Movie poster for drama/thriller feature

We need a movie poster for an edgy microbudget, drama/thriller feature called Stumbling My Road Past Dawn and is about a “night in the life” of an escort and her driver after she discovers that her mother, who was caring for her daughter, has died. She has just one night to raise the money to cover the arrears on her mother’s mortgage and return to collect her daughter before her very religious aunt calls Children’s Aid. On top of that she has to enlist the help of her new driver who is also very religious and hates her because she’s a “whore”. He is only doing this job because, as a Cuban refugee, he has had to take a job with his uncle, who is head of security at the agency, in order to pay him back what it cost to bring him to Canada. So, at the core of the story is this relationship between two people who hate each other but are stuck together in a car for an entire night. The third character is the uncle - head of security - who becomes increasingly "dark" and violent as the night goes on as he feels he is losing the loyalty of his nephew to a sex worker who is ripping off his boss.

So, that's the backdrop to the story.

Now, we want the poster to reflect that this is a scrappy, edgy little film, a bit controversial (just the title alone, obviously). Some of our inspiration for the poster are the kind of minimalist designs from French New Wave films (examples uploaded). The title itself can either be written out in toto or you could put the acronym in bold letters - SMRPD - with their meaning smaller below it. You can play with it, anyway, to come up with some cool. I've also included stills from the film of the three main characters - Marisol, the lead/star, Tomas (her driver) and Ignacio, the antaonist/uncle. You can crop these to make them work. I just left them full size so that you'd have more options.

If you have questions, don't hesitate to ask.

best
Derek

Target Market(s)

indie film goers, younger, city-based, hipster demographic

Industry/Entity Type

Film Production

Font styles to use
Sans Serif

Colors

Designer to choose colors to be used in the design.

Requirements
Must have
• A great look, the title, and some credits:
• tagline: one night can change your whole world
• A film by Bridget Oldcastle & Derek Fenwold
• With
• Ingrid Tolmachova
• Esteban Morales-Quiroga
• Raul Caceres Villalobos
• Cinematography
• Nate Corbell
• Produced by:
• Crooked Lantern Productions
• Pinecrest Studios
• and a credit block with:
• Bridget Oldcastle ... co-producer
• Ingrid Tolmachova ... co-producer
• Esteban Morales-Quiroga ... co-producer
• Gavin Trout ... co-producer
• Derek Fenwold ... co-producer
• Editing by
• Dana McGivney
• Production Design by
• Tiago Mendes Rocha
• Wendy Calder ... key makeup artist
• Priscilla Novak ... makeup artist Production Management
• Tessa Kimball ... production manager Second Unit Director or Assistant Director
• Tessa Kimball ... first assistant director Sound Department
• Ben Yardley ... sound editor
• Kevin Santoso ... sound recordist Stunts
• Raul Caceres Villalobos ... action coordinator
• Carl Pembry ... still photographer
• Fiona Beckett ... swing
• Monica Thorne ... still photographer
• Giulia Marchetti ... swing Costume and Wardrobe Department
• Nora Fairclough ... wardrobe
• Petra Holub ... wardrobe supervisor Transportation Department
• Rosalind Tapley ... craft service
• Maya Finch ... script supervisor
• Paolo Reyes ... production assistant
• Lucia Navarro ... craft service

```html
<!DOCTYPE html>
<html lang="en">
<head>
<meta charset="utf-8">
<title>Stumbling My Road Past Dawn — Poster</title>
<link href="https://fonts.googleapis.com/css2?family=Montserrat:wght@800&family=Oswald:wght@400;500&display=swap" rel="stylesheet">
<style>
  :root{
    --ink:#1d1d1f;
    --paper:#f7f6f3;
    --white:#ffffff;
    --gold:#c9a24a;
    --night-teal:#1f3b3a;
    --night-red:#7a2a24;
    --night-violet:#3a2b4a;
    --muted:#6c6c6c;
  }
  *{margin:0;padding:0;box-sizing:border-box}
  html,body{width:811px;height:1200px;overflow:hidden;background:var(--paper)}
  .poster{position:relative;width:811px;height:1200px;overflow:hidden;font-family:"Oswald",sans-serif;color:var(--white)}

  .scene{position:absolute;inset:0;
    background:
      radial-gradient(ellipse 120px 90px at 560px 280px, rgba(240,200,120,.55), transparent),
      radial-gradient(ellipse 180px 140px at 120px 100px, rgba(80,160,140,.6), transparent),
      radial-gradient(ellipse 260px 120px at 420px 390px, rgba(200,70,50,.7), transparent),
      radial-gradient(ellipse 200px 260px at 80px 860px, rgba(150,80,170,.55), transparent),
      linear-gradient(180deg,var(--night-teal) 0%,#2b2a2a 30%,var(--night-red) 38%,#2a2424 55%,var(--night-violet) 75%,#2a2530 100%);}
  .portrait{position:absolute;border-radius:2px}
  .portrait--lead{left:335px;top:0;width:310px;height:360px;
    background:radial-gradient(ellipse at 55% 45%, #d9b39a 0%, #9a7058 35%, rgba(40,30,30,.0) 75%);}
  .portrait--driver{left:270px;top:390px;width:270px;height:300px;
    background:radial-gradient(ellipse at 50% 40%, #8a6a58 0%, #4a3a34 45%, rgba(30,30,30,0) 80%);}
  .portrait--uncle{left:320px;top:690px;width:270px;height:320px;
    background:radial-gradient(ellipse at 50% 35%, #8d6450 0%, #3c2e2c 50%, rgba(20,20,30,0) 85%);}

  .fade{position:absolute;left:0;right:0;top:950px;bottom:0;
    background:linear-gradient(180deg,rgba(247,246,243,0) 0%,rgba(247,246,243,.85) 45%,var(--paper) 70%);}

  .streaks{position:absolute;inset:0}

  .presenter{position:absolute;top:20px;left:0;right:0;text-align:center;
    font-family:"Montserrat",sans-serif;font-size:10px;letter-spacing:.12em;line-height:1.35;text-transform:uppercase}

  .tagline{position:absolute;left:14px;font-family:"Montserrat",sans-serif;font-weight:800;
    font-size:43px;line-height:1;letter-spacing:.005em;text-transform:uppercase}
  .tagline--1{top:228px}
  .tagline--2{top:414px}
  .tagline--3{top:574px;line-height:1.05}

  .title{position:absolute;left:0;right:0;top:872px;text-align:center;
    font-family:"Oswald",sans-serif;font-weight:500;font-size:128px;line-height:1;letter-spacing:.14em;color:var(--white)}
  .subtitle{position:absolute;left:0;right:0;top:1030px;text-align:center;
    font-family:"Oswald",sans-serif;font-weight:400;font-size:25px;letter-spacing:.08em;color:var(--muted);text-transform:uppercase}
  .subtitle .initial{color:var(--gold)}

  .credits{position:absolute;left:20px;right:20px;top:1075px;text-align:center;color:var(--ink);
    font-family:"Oswald",sans-serif;text-transform:uppercase}
  .credits p{font-size:10.5px;line-height:1.3;letter-spacing:.06em;white-space:nowrap}
  .credits small{font-size:6.5px;letter-spacing:.06em}
  .credits .crew{font-size:7.5px;line-height:1.45;letter-spacing:.04em}
  .credits .crew small{font-size:5.5px}
</style>
</head>
<body>
<main class="poster">
  <div class="scene" role="img" aria-label="Night street scene with blurred city lights seen through a car"></div>
  <div class="portrait portrait--lead" role="img" aria-label="Still of Marisol, the lead, at night"></div>
  <div class="portrait portrait--driver" role="img" aria-label="Still of Tomas, the driver, at the wheel"></div>
  <div class="portrait portrait--uncle" role="img" aria-label="Still of Ignacio, the uncle"></div>

  <svg class="streaks" width="811" height="1200" viewBox="0 0 811 1200" aria-hidden="true">
    <g fill="#ffffff" fill-opacity=".9">
      <polygon points="90,18 760,12 790,22 770,30 300,36 110,34 70,28"/>
      <polygon points="120,62 540,58 560,66 300,72 100,70"/>
      <polygon points="470,128 811,120 811,140 640,142 480,138"/>
      <polygon points="0,258 330,250 520,262 600,268 420,280 80,282 0,276"/>
      <polygon points="0,296 150,292 350,300 160,308 0,306"/>
      <polygon points="560,340 811,332 811,352 700,356 580,350"/>
      <polygon points="0,448 380,440 240,456 0,458"/>
      <polygon points="0,498 260,492 440,500 200,512 0,510"/>
      <polygon points="420,552 811,540 811,572 640,578 460,566"/>
      <polygon points="160,588 780,580 811,592 700,600 300,604 150,598"/>
      <polygon points="0,746 200,740 310,750 100,756 0,754"/>
      <polygon points="0,786 380,780 430,790 200,798 0,796"/>
      <polygon points="560,870 811,862 811,880 650,884"/>
      <polygon points="0,990 811,980 811,1012 600,1016 0,1010"/>
    </g>
  </svg>

  <div class="fade"></div>

  <p class="presenter">Crooked Lantern Productions &amp;<br>Pinecrest Studios<br>present</p>

  <h2 class="tagline tagline--1">One<br>Night</h2>
  <h2 class="tagline tagline--2">Can<br>Change</h2>
  <h2 class="tagline tagline--3">Your<br>Whole<br>World.</h2>

  <h1 class="title">S.M.R.P.D</h1>
  <p class="subtitle"><span class="initial">S</span>tumbling My Road Past Dawn</p>

  <section class="credits">
    <p><small>A film by</small> Bridget Oldcastle &amp; Derek Fenwold</p>
    <p><small>With</small> Ingrid Tolmachova &nbsp;Esteban Morales-Quiroga &nbsp;Raul Caceres Villalobos</p>
    <p><small>Produced by</small> Crooked Lantern Productions &amp; Pinecrest Studios &nbsp;<small>Cinematography</small> Nate Corbell</p>
    <p><small>Co-produced by</small> Bridget Oldcastle &nbsp;Ingrid Tolmachova &nbsp;Esteban Morales-Quiroga &nbsp;Gavin Trout &nbsp;Derek Fenwold</p>
    <p class="crew"><small>Editing by</small> Dana McGivney &nbsp;<small>Production design by</small> Tiago Mendes Rocha &nbsp;<small>Key makeup artist</small> Wendy Calder &nbsp;<small>Makeup artist</small> Priscilla Novak</p>
    <p class="crew"><small>Production manager</small> Tessa Kimball &nbsp;<small>First assistant director</small> Tessa Kimball &nbsp;<small>Sound editor</small> Ben Yardley &nbsp;<small>Sound recordist</small> Kevin Santoso</p>
    <p class="crew"><small>Action coordinator</small> Raul Caceres Villalobos &nbsp;<small>Still photographers</small> Carl Pembry &nbsp;Monica Thorne &nbsp;<small>Swing</small> Fiona Beckett &nbsp;Giulia Marchetti</p>
    <p class="crew"><small>Wardrobe</small> Nora Fairclough &nbsp;<small>Wardrobe supervisor</small> Petra Holub &nbsp;<small>Craft service</small> Rosalind Tapley &nbsp;Lucia Navarro &nbsp;<small>Script supervisor</small> Maya Finch &nbsp;<small>Production assistant</small> Paolo Reyes</p>
  </section>
</main>
</body>
</html>
```